Women & Wealth Program Needs Invitation Design

We are looking for an invitation and save the date for a Women & Wealth Program that we host called Blossomry (logo attached)
I have uploaded an example of previous invitations we have had for Blossomry events. We’d like for the invitation to be feminine but not too cutesy.

We like the size of 8 ½ x 3 ¾ but would be open to a traditional 5x7—2 sided. We will be mailing out a paper invitation and sending out an electronic save the date and invitation.

The program title is “75 is the new 62—how to blossomry(use logo) and plan for longevity.”
Our idea for the front is to have a birthday cake possibly with “75 is the new 62” on the cake with the tagline underneath it.

On the back we would like the following information included:
Join Delia Marsh in this interactive program as she discusses how to eat your cake and have your retirement too. Learn why 75 is the new 62 and how planning for longevity, investing in your own human capital, and finding your next act will help you blossomry in this new age of retirement.

The program will be on Wednesday, February 3 from 6-8pm at MillWarden, 4617 Pebblecrest Rd., Valley View, OH 44187
Wine & hors d’oevres will be served.
RSVP by Tuesday, January 26 to Roxanne Walsh at 330-471-6093 or email rwalsh@pqbwealth-example.com

We must include our business logo, contact information, and disclaimer: Delia T. Marsh, CFP®, AIF® 918 Harrowgate Drive, Suite 410, Akron, OH 44396 www.pqbwealth-example.com
Securities and advisory services offered through Halvern Partners LLC, member FINRA/SIPC. Halvern is under separate ownership from any other entity. (this disclaimer can be as small as 8pt font)

Reason: We would like to have more choices for this unique women's event! Don't be afraid to be edgy!

Target Market(s)

Professional Women-Doctors, Accountants, Business Owners.
Women close to retirement, retired women.

Industry/Entity Type

Financial Service

Font styles to use
Sans Serif
Decorative
Script

Requirements
Must have
• We must include our business logo, contact information, and disclaimer: Delia T. Marsh, CFP®, AIF® 918 Harrowgate Drive, Suite 410, Akron, OH 44396 www.pqbwealth-example.com
• Securities and advisory services offered through Halvern Partners LLC, member FINRA/SIPC. Halvern is under separate ownership from any other entity. (this disclaimer can be as small as 8pt font)
• The program will be on Wednesday, February 3 from 6-8pm at MillWarden, 4617 Pebblecrest Rd., Valley View, OH 44187
• Wine & hors d’oevres will be served.
• RSVP by Tuesday, January 26 to Roxanne Walsh at 330-471-6093 or email rwalsh@pqbwealth-example.com
Nice to have
• The front possibly have a birthday cake with the program title written on it?

```html
<!DOCTYPE html>
<html lang="en">
<head>
<meta charset="utf-8">
<title>Save the Date – How to Blossomry &amp; Plan for Longevity</title>
<link rel="stylesheet" href="https://fonts.googleapis.com/css2?family=Roboto+Condensed:ital,wght@0,300;0,700;1,300;1,700&family=Great+Vibes&display=swap">
<style>
  :root {
    --rose: #c94a82;
    --rose-deep: #b23a6f;
    --ink: #241a1e;
    --paper: #ffffff;
    --lace-light: #f4f1f2;
    --lace-mid: #d9d3d6;
    --cake-pink: #e9a9c7;
    --cake-cream: #f7e6ee;
  }
  html, body {
    margin: 0;
    padding: 0;
    width: 1200px;
    height: 518px;
    overflow: hidden;
    background: var(--paper);
  }
  .save-the-date {
    display: block;
    width: 1200px;
    height: 518px;
  }
  .sans { font-family: "Roboto Condensed", "Arial Narrow", sans-serif; }
  .script { font-family: "Great Vibes", cursive; }
  .event-day { fill: var(--ink); font-weight: 700; font-size: 42px; letter-spacing: -0.5px; }
  .event-time { fill: var(--ink); font-weight: 300; font-size: 42px; letter-spacing: -0.5px; }
  .event-time .strong { font-weight: 700; }
  .event-time .strong-italic { font-weight: 700; font-style: italic; }
  .event-time .light-italic { font-weight: 300; font-style: italic; }
  .title-lead { fill: var(--paper); font-weight: 700; font-size: 29px; }
  .title-name { fill: var(--paper); font-size: 72px; }
  .title-plan { fill: var(--paper); font-weight: 700; font-size: 40px; letter-spacing: -0.5px; }
  .title-plan .light-italic { font-weight: 300; font-style: italic; }
  .title-tail { fill: var(--paper); font-weight: 300; font-size: 42px; letter-spacing: 0.5px; }
  .stamp { fill: var(--paper); font-size: 27px; }
  .stamp .light { font-weight: 300; }
  .stamp .bold-italic { font-weight: 700; font-style: italic; }
  .stamp .bold { font-weight: 700; }
</style>
</head>
<body>
<svg class="save-the-date" viewBox="0 0 1200 518" xmlns="http://www.w3.org/2000/svg">
  <defs>
    <linearGradient id="lace-tone" x1="0" y1="0" x2="1" y2="1">
      <stop offset="0" stop-color="var(--lace-light)"/>
      <stop offset="1" stop-color="var(--lace-mid)"/>
    </linearGradient>
    <radialGradient id="cake-tone" cx="0.5" cy="0.55" r="0.6">
      <stop offset="0" stop-color="var(--cake-cream)"/>
      <stop offset="1" stop-color="var(--cake-pink)"/>
    </radialGradient>
  </defs>

  <!-- header lace band -->
  <rect class="lace-band" x="0" y="0" width="1200" height="135" fill="url(#lace-tone)"
        role="img" aria-label="Black and white damask pattern with a black ribbon lattice and pink buttons"/>

  <!-- rose field -->
  <rect class="rose-field" x="0" y="135" width="1200" height="383" fill="var(--rose)"/>

  <!-- base triangle behind the frame -->
  <polygon class="stamp-triangle" points="435,518 753,518 600,353" fill="var(--ink)"/>

  <!-- framed inverted triangle -->
  <polygon class="frame-outer" points="381,89 819,89 600,450" fill="var(--paper)"/>
  <polygon class="frame-rule" points="410,106 790,106 600,422" fill="var(--ink)"/>
  <polygon class="frame-inner" points="432,119 768,119 600,397" fill="var(--paper)"/>

  <!-- cake photograph area -->
  <rect class="cake-photo" x="505" y="115" width="152" height="167" rx="30" fill="url(#cake-tone)"
        role="img" aria-label="Photo of a pink heart-shaped cake topped with strawberries and cream, with a chocolate plaque reading 75 is the new 62"/>

  <!-- event date -->
  <text class="sans event-day" x="85" y="305">WEDNESDAY</text>
  <text class="sans event-time" x="85" y="340">FEB<tspan class="strong">3</tspan>\<tspan class="strong-italic">6-8</tspan><tspan class="light-italic">PM</tspan></text>

  <!-- program title -->
  <text class="sans title-lead" x="1064" y="279" text-anchor="end">HOW TO</text>
  <text class="script title-name" x="840" y="306">blossomry</text>
  <text class="sans title-plan" x="840" y="340">&amp;PLAN<tspan class="light-italic">FOR</tspan></text>
  <text class="sans title-tail" x="840" y="371">LONGEVITY</text>

  <!-- save the date -->
  <text class="sans stamp" x="600" y="497" text-anchor="middle"><tspan class="light">SAVE</tspan><tspan class="bold-italic">THE</tspan><tspan class="bold">DATE</tspan></text>
</svg>
</body>
</html>
```